Mortgage broker flyer

I need a flyer to advertise who we are, what we do and why people should use us. and with a call to action. Our service is free, and we have over 35 different lenders that we can source loans from. we offer a mobile service. we will visit people anywhere anytime to discuss their needs. The flyers are to be placed in real estate agencies as well as put in people's letter boxes

Target Market(s)

clients looking at purchasing property - going through open homes.

Industry/Entity Type

Finance

Colors
add136
cadf82
aaaaaa
959595

Requirements
Must have
• Service is free
• won KRD broker of the year 2014,2015
• Veltrona insurance - Free 90 days building insurance through Veltrona
• Logo colours

```html
<!DOCTYPE html>
<html lang="en">
<head>
<meta charset="utf-8">
<title>Northgate Finance Solutions – Mortgage Broking Flyer</title>
<link href="https://fonts.googleapis.com/css2?family=Open+Sans:wght@400;600&family=Roboto:wght@300;400&family=Playball&display=swap" rel="stylesheet">
<style>
  :root {
    --green: #add136;
    --green-soft: #cadf82;
    --grey-light: #aaaaaa;
    --grey: #959595;
    --grey-text: #7a7a7a;
    --band-light: #f1f1f1;
    --white: #ffffff;
    --page-bg: #e9e9e6;
  }
  * { box-sizing: border-box; margin: 0; padding: 0; }
  html, body { width: 960px; height: 1200px; overflow: hidden; background: var(--page-bg); }
  .flyer {
    position: absolute; left: 77px; top: 30px;
    width: 806px; height: 1140px; background: var(--white);
    overflow: hidden; box-shadow: 0 4px 18px rgba(0,0,0,.18);
    font-family: "Open Sans", sans-serif;
  }
  .abs { position: absolute; }

  /* hero */
  .hero-photo {
    left: 0; top: 0; width: 806px; height: 474px;
    background: linear-gradient(180deg, #e6eef0 0%, #cfdcc8 28%, #7fae4a 45%, #6d9a3f 62%, #98a88a 82%, #b8b9b0 100%);
  }
  .hero-car {
    right: 0; top: 130px; width: 250px; height: 344px;
    background: linear-gradient(160deg, #f5f5f5, #d8dadb);
  }
  .brand-card {
    left: 49px; top: 0; width: 347px; height: 163px;
    background: linear-gradient(180deg, #ffffff, #f1f1f1);
    border-radius: 0 0 6px 6px; box-shadow: 0 3px 8px rgba(0,0,0,.2);
    display: flex; align-items: center; gap: 14px; padding-left: 22px;
  }
  .brand-mark { width: 40px; height: 40px; border-radius: 50%; background: var(--green); flex: none; }
  .brand-name { font-family: "Open Sans", sans-serif; font-weight: 600; color: var(--green); font-size: 30px; line-height: 1.1; }
  .hero-quote {
    left: 26px; top: 312px; color: var(--white);
    font-family: "Roboto", sans-serif; font-weight: 300; font-size: 39px; line-height: 48px;
    text-shadow: 0 1px 3px rgba(0,0,0,.25);
  }
  .hero-quote span { display: block; padding-left: 30px; }

  /* services */
  .services { left: 0; top: 474px; width: 806px; height: 225px; background: var(--band-light); }
  .service { position: absolute; top: 0; width: 268px; margin-left: -134px; text-align: center; }
  .service-icon {
    width: 106px; height: 106px; border-radius: 50%; background: var(--green);
    margin: 20px auto 0; display: flex; align-items: center; justify-content: center;
  }
  .service-title { margin-top: 22px; font-weight: 600; font-size: 21px; color: var(--grey-text); }
  .service-text { font-size: 16px; line-height: 20px; color: var(--grey-text); text-transform: uppercase; }

  /* commitments */
  .commitments { left: 0; top: 699px; width: 806px; height: 155px; background: var(--grey); }
  .tab {
    left: 0; top: 14px; width: 49px; height: 130px; background: var(--green);
    border-radius: 0 4px 4px 0; display: flex; align-items: center; justify-content: center;
  }
  .tab-label { transform: rotate(-90deg); white-space: nowrap; color: var(--white); font-weight: 600; font-size: 22px; }
  .commit-list {
    left: 69px; top: 30px; list-style: none; color: var(--white);
    font-family: "Roboto", sans-serif; font-weight: 300; font-size: 20.5px; line-height: 26.5px;
  }
  .commit-list li::before { content: "\2022"; margin-right: 4px; }

  /* call to action */
  .cta { left: 0; top: 854px; width: 806px; height: 286px; background: var(--green); }
  .cta-title { left: 31px; top: 10px; font-family: "Playball", cursive; color: var(--white); font-size: 36px; }
  .cta-lead { left: 31px; top: 58px; color: var(--white); font-family: "Roboto", sans-serif; font-size: 16.5px; line-height: 23px; }
  .cta-pill {
    left: 0; top: 101px; width: 500px; height: 48px; background: var(--white);
    border-radius: 0 8px 8px 0; box-shadow: 0 3px 6px rgba(0,0,0,.2);
    font-family: "Roboto", sans-serif; color: var(--grey-text); font-size: 23px;
    display: flex; align-items: center; justify-content: center;
  }
  .contact-list { left: 31px; top: 166px; list-style: none; color: var(--white); font-size: 16px; line-height: 22.3px; }
  .contact-list li { display: flex; align-items: center; gap: 9px; }
  .contact-list .strong { font-weight: 600; font-size: 17.5px; }
  .contact-icon { width: 16px; height: 16px; flex: none; }
  .team-photo {
    left: 594px; top: 31px; width: 159px; height: 156px;
    background: linear-gradient(180deg, #b9c89a 0%, #2a2a2a 45%, #1c1c1c 100%);
    border-radius: 70px 70px 0 0;
  }
  .award {
    left: 563px; top: 186px; width: 215px; height: 100px; background: var(--white);
    border-radius: 6px 6px 0 0; padding: 16px 14px 0;
  }
  .award-head { display: flex; align-items: center; gap: 10px; }
  .award-mark { width: 42px; height: 42px; border-radius: 50%; background: var(--grey-light); flex: none; }
  .award-name { font-weight: 600; font-size: 20px; color: #333; }
  .award-text { margin-top: 4px; text-align: center; font-weight: 600; font-size: 10px; line-height: 12px; color: #1f3c88; }
</style>
</head>
<body>
<main class="flyer">
  <section>
    <div class="abs hero-photo" role="img" aria-label="Photo of a person's legs in canvas sneakers resting out of a car window beside a grassy park with trees"></div>
    <div class="abs hero-car" role="img" aria-label="White car door with side mirror"></div>
    <div class="abs brand-card">
      <span class="brand-mark"></span>
      <div class="brand-name">Northgate<br>Finance Solutions</div>
    </div>
    <p class="abs hero-quote">“Just&nbsp; sit back,<span>and let us handle Everything”</span></p>
  </section>

  <section class="abs services">
    <div class="service" style="left:145px">
      <div class="service-icon">
        <svg width="62" height="62" viewBox="0 0 62 62" fill="none" stroke="#fff" stroke-width="4" stroke-linejoin="round">
          <path d="M17 28 L31 15 L45 28 M21 25 V40 H41 V25"/><rect x="28" y="31" width="6" height="9" fill="#fff" stroke="none"/>
          <path d="M6 34 Q8 50 31 54 Q54 50 56 34" stroke-linecap="round"/>
        </svg>
      </div>
      <h3 class="service-title">VELTRONA INSURANCE</h3>
      <p class="service-text">Free 90 days building<br>insurance through Veltrona</p>
    </div>
    <div class="service" style="left:403px">
      <div class="service-icon">
        <svg width="76" height="40" viewBox="0 0 76 40" fill="none" stroke="#fff" stroke-width="8">
          <rect x="5" y="6" width="36" height="28" rx="14"/><rect x="35" y="6" width="36" height="28" rx="14"/>
        </svg>
      </div>
      <h3 class="service-title">FREE</h3>
      <p class="service-text">Mobile&nbsp; mortgage<br>broking service</p>
    </div>
    <div class="service" style="left:662px">
      <div class="service-icon">
        <svg width="66" height="50" viewBox="0 0 66 50" fill="#fff">
          <rect x="14" y="10" width="38" height="24" rx="2"/>
          <circle cx="33" cy="20" r="6" fill="#add136"/>
          <path d="M2 14 L12 8 L14 40 L6 40 Z M64 14 L54 8 L52 40 L60 40 Z"/>
          <rect x="16" y="36" width="34" height="4"/>
        </svg>
      </div>
      <h3 class="service-title">OVER 35 LENDERS</h3>
      <p class="service-text">That we can source<br>loans from</p>
    </div>
  </section>

  <section class="abs commitments">
    <div class="abs tab"><span class="tab-label">WE WILL</span></div>
    <ul class="abs commit-list">
      <li>Visit people anywhere anytime to discuss their needs.</li>
      <li>Show you what our over 35 lenders have to offer.</li>
      <li>Advice the most suitable loan for your needs.</li>
      <li>Guide you through the purchase or refinance process, one step at a time.</li>
    </ul>
  </section>

  <section class="abs cta">
    <h2 class="abs cta-title">We're on your side!</h2>
    <p class="abs cta-lead">Why have one bank or lender visit you,<br>when you can have access to over 35 at once?</p>
    <div class="abs cta-pill">Arrange an appointment today...</div>
    <ul class="abs contact-list">
      <li class="strong"><svg class="contact-icon" viewBox="0 0 16 16"><circle cx="8" cy="8" r="8" fill="#8fb02a"/><path d="M5 4 L7 4 L7.5 6.5 L6.5 7.3 Q7.5 9 9 9.6 L9.8 8.6 L12 9.2 L12 11 Q7 12 4.5 6 Z" fill="#fff"/></svg>07 3000 4821</li>
      <li class="strong"><svg class="contact-icon" viewBox="0 0 16 16"><circle cx="8" cy="8" r="8" fill="#8fb02a"/><rect x="5.5" y="3.5" width="5" height="9" rx="1" fill="#fff"/></svg>0400 123 987</li>
      <li><svg class="contact-icon" viewBox="0 0 16 16"><circle cx="8" cy="8" r="8" fill="#8fb02a"/><path d="M8 3 A3 3 0 0 1 11 6 Q11 8 8 13 Q5 8 5 6 A3 3 0 0 1 8 3 Z" fill="#fff"/></svg>Po Box 2210, Elmridge. QLD. 4500.</li>
      <li><svg class="contact-icon" viewBox="0 0 16 16"><circle cx="8" cy="8" r="8" fill="#8fb02a"/><rect x="4" y="5" width="8" height="6" fill="#fff"/><path d="M4 5 L8 8.5 L12 5" stroke="#8fb02a" fill="none"/></svg>info@northgatefs.com.au</li>
      <li><svg class="contact-icon" viewBox="0 0 16 16"><circle cx="8" cy="8" r="8" fill="#8fb02a"/><circle cx="8" cy="8" r="4.5" fill="none" stroke="#fff" stroke-width="1.4"/><path d="M3.5 8 H12.5 M8 3.5 V12.5" stroke="#fff" stroke-width="1"/></svg>northgatefs.com.au</li>
    </ul>
    <div class="abs team-photo" role="img" aria-label="Photo of two brokers in tuxedos holding glass award trophies"></div>
    <div class="abs award">
      <div class="award-head"><span class="award-mark"></span><span class="award-name">KRD</span></div>
      <p class="award-text">Mortgage Broker of the Year<br>2014&nbsp; 2015</p>
    </div>
  </section>
</main>
</body>
</html>
```